Business Card Design - Brightfold Dwellings

Hi there,

We would like a business card for our new venture, Brightfold Dwellings.

We are based in Western Australia and specialise in taking tired, old properties and making them look new again. We aim to create enjoyably liveable homes for young families in particular.

Product pricing is mid range i.e. appliances, furnishings, fixtures (not top end but not cheap either)

Our work is primarily cosmetic renovation (approx. 80%) and the rest construction (approx 20%).

We would like a business card that conveys the following:
- clean, simplistic/minimalistic design
- modern, contemporary style
- a touch of funk/uniqueness
- appealing to both females and males
- professionalism

I have uploaded our logo in grey or green, I do not mind which one you choose to use (please use either coloured logo on the pure white background not the white on colour version).

Details to include on the business card are:
Names: Corina Maddox and Pete Okonbrie
Mobile: 0417 362 908
Email: info@brightfolddwellings.com.au
Website: www.brightfolddwellings.com.au (note: this website is currently being developed)
Note: We will provide final details such as mobile number and names on on selection of successful design)

On the other side of the card please include a line similar to "We buy tired, un-renovated properties and sell them looking new again!"

The business card will also need to include the following "ABN 47 219 635 104" which is our Australian Business Number (again the actual number will be provided on selection of successful design). We would like this number somewhere near our name Brightfold Dwellings but in much smaller text.

The purpose of the business cards will be to give to suppliers, real estate agents, people wanting assistance in locating a property in need of renovation and potential buyers.

Thank you and please let me know if you have any further questions.

```html
<!DOCTYPE html>
<html lang="en">
<head>
<meta charset="utf-8">
<title>Brightfold Dwellings – Business Card</title>
<link href="https://fonts.googleapis.com/css2?family=Lato:wght@400;700;900&display=swap" rel="stylesheet">
<style>
  :root {
    --lime: #8dc63f;
    --lime-dark: #76ad2b;
    --ink: #1c1c1c;
    --paper: #ffffff;
    --stage: #e4e5e3;
    --muted: #2b2b2b;
    --soft: #6a6a6a;
  }
  * { box-sizing: border-box; margin: 0; padding: 0; }
  html, body {
    width: 1200px; height: 900px; overflow: hidden;
    background: var(--stage);
    font-family: "Lato", sans-serif;
  }
  .canvas { position: relative; width: 1200px; height: 900px; }

  .card {
    position: absolute;
    width: 600px; height: 343px;
    border-radius: 4px;
    overflow: hidden;
    box-shadow: 0 10px 30px rgba(0,0,0,.18);
  }

  /* Back side */
  .card--back {
    left: 50px; top: 60px;
    background: var(--lime);
    color: var(--paper);
    display: flex; flex-direction: column; align-items: center; justify-content: center;
    text-align: center;
  }
  .brand-name {
    font-family: "Lato", sans-serif;
    font-weight: 400;
    font-size: 44px;
    letter-spacing: .5px;
    line-height: 1;
  }
  .card--back .brand-name { color: var(--paper); margin-bottom: 46px; }
  .tagline {
    font-weight: 900;
    font-size: 17px;
    letter-spacing: 1px;
    line-height: 1.45;
    text-transform: uppercase;
  }

  /* Front side */
  .card--front {
    left: 550px; top: 497px;
    background: var(--paper);
  }
  .brand-block {
    position: absolute; left: 0; right: 0; top: 92px;
    text-align: center;
  }
  .card--front .brand-name { color: var(--lime); }
  .abn {
    margin-top: 8px;
    color: var(--soft);
    font-size: 10px;
    font-weight: 400;
    letter-spacing: 1.2px;
    text-transform: uppercase;
  }
  .person {
    position: absolute; right: 34px; top: 168px; text-align: right;
  }
  .person__name {
    color: var(--lime); font-weight: 900; font-size: 19px; letter-spacing: .3px;
    text-transform: uppercase; line-height: 1.1;
  }
  .person__role {
    color: var(--muted); font-size: 14px; letter-spacing: .8px; text-transform: uppercase;
  }

  .contact-tab {
    position: absolute; left: 0; top: 224px;
    width: 40px; height: 100px;
    background: var(--lime);
    border-radius: 0 9px 9px 0;
    display: flex; flex-direction: column; align-items: center; justify-content: space-around;
    padding: 6px 0;
  }
  .contact-tab svg { width: 20px; height: 20px; }

  .contact-list {
    position: absolute; left: 58px; top: 228px;
    list-style: none;
    color: var(--ink); font-weight: 700; font-size: 16px;
  }
  .contact-list li { height: 31px; line-height: 31px; }

  .card-foot { position: absolute; left: 0; bottom: 0; width: 600px; height: 40px; }
</style>
</head>
<body>
<main class="canvas">

  <section class="card card--back" aria-label="Card back">
    <p class="brand-name">Brightfold Dwellings</p>
    <p class="tagline">We buy tired, un-renovated properties<br>&amp; sell them looking new again!</p>
  </section>

  <section class="card card--front" aria-label="Card front">
    <div class="brand-block">
      <p class="brand-name">Brightfold Dwellings</p>
      <p class="abn">ABN 47 219 635 104</p>
    </div>

    <div class="person">
      <p class="person__name">Corina Maddox</p>
      <p class="person__role">Director</p>
    </div>

    <div class="contact-tab" aria-hidden="true">
      <svg viewBox="0 0 20 20" fill="none" stroke="#fff" stroke-width="1.6">
        <rect x="5" y="1.5" width="10" height="17" rx="1.5"/>
        <line x1="8.5" y1="16" x2="11.5" y2="16"/>
      </svg>
      <svg viewBox="0 0 20 20" fill="none" stroke="#fff" stroke-width="1.6">
        <rect x="1.5" y="4.5" width="17" height="11" rx="1"/>
        <polyline points="1.5,4.5 10,11 18.5,4.5"/>
      </svg>
      <svg viewBox="0 0 20 20" fill="none" stroke="#fff" stroke-width="1.6">
        <circle cx="10" cy="10" r="8"/>
        <ellipse cx="10" cy="10" rx="3.5" ry="8"/>
        <line x1="2" y1="10" x2="18" y2="10"/>
      </svg>
    </div>

    <ul class="contact-list">
      <li>0417 362 908</li>
      <li>info@brightfolddwellings.com.au</li>
      <li>www.brightfolddwellings.com.au</li>
    </ul>

    <svg class="card-foot" viewBox="0 0 600 40" preserveAspectRatio="none" aria-hidden="true">
      <path d="M0 40 L0 32 L470 20 L470 40 Z" fill="var(--lime)"/>
      <path d="M462 40 L470 20 Q474 6 492 6 L600 6 L600 40 Z" fill="var(--ink)"/>
    </svg>
  </section>

</main>
</body>
</html>
```